Business card design needed

I have a leadership coaching and consultancy business which specialises in the education sector. I would like a clean, professional design). The design needs to speak to strength, support, new learning, connections & a growth mindest.

I am also looking for a unique LOGO. This is very important.

Target Market(s)

Educational Leaders & executives

Industry/Entity Type

Leadership

Contact Information for Business Card

Miranda Voss
Principal Coach & Consultant
Miranda Voss Coaching & Consulting
0491 362 815
miranda.voss@quillmail.example
I also would like my facebook, twitter and linkedin accounts to appear

Logo styles of interest
Lettermark Logo
Requirements
Must have
• A 2 sided business card with contact details on the back
A logo

```html
<!DOCTYPE html>
<html lang="en">
<head>
<meta charset="utf-8">
<title>Miranda Voss Coaching &amp; Consulting – Business Card</title>
<link rel="stylesheet" href="https://fonts.googleapis.com/css2?family=Roboto+Condensed:wght@400;700&family=Questrial&display=swap">
<style>
  :root {
    --orange: #f05a24;
    --orange-light: #f6a07a;
    --blue: #2a6aa3;
    --ink: #111111;
    --white: #ffffff;
  }
  html, body {
    margin: 0;
    padding: 0;
    width: 1200px;
    height: 720px;
    overflow: hidden;
    background: var(--white);
  }
  .card {
    position: relative;
    width: 1200px;
    height: 720px;
    background: var(--white);
    overflow: hidden;
    font-family: "Roboto Condensed", "Arial Narrow", sans-serif;
  }

  /* Brand block */
  .brand {
    position: absolute;
    left: 32px;
    top: 70px;
    width: 320px;
    text-align: center;
  }
  .brand-mark {
    display: block;
    width: 128px;
    height: 128px;
    margin: 0 auto 8px;
    border-radius: 50%;
    background: var(--orange);
  }
  .brand-name {
    margin: 0;
    color: var(--blue);
    font-weight: 700;
    line-height: 1.05;
  }
  .brand-name .line-name { display: block; font-size: 50px; }
  .brand-name .line-trade { display: block; font-size: 30px; }

  /* Person */
  .person {
    position: absolute;
    left: 690px;
    top: 210px;
    width: 460px;
    text-align: center;
    font-family: "Questrial", "Century Gothic", sans-serif;
  }
  .person-name {
    margin: 0;
    color: var(--blue);
    font-size: 30px;
    letter-spacing: 2px;
    font-weight: 400;
    text-transform: uppercase;
  }
  .person-role {
    margin: 18px 0 0;
    color: var(--ink);
    font-size: 25px;
    font-variant: small-caps;
    letter-spacing: 1px;
  }

  /* Divider and contact band */
  .divider {
    position: absolute;
    left: 0;
    top: 351px;
    width: 1200px;
    height: 5px;
    background: var(--orange);
  }
  .contact-band {
    position: absolute;
    left: 0;
    top: 361px;
    width: 1200px;
    height: 359px;
    background: var(--orange);
  }
  .contact-band::before {
    content: "";
    position: absolute;
    left: 0;
    top: 0;
    width: 100%;
    height: 7px;
    background: repeating-linear-gradient(-60deg, var(--orange-light) 0 8px, transparent 8px 20px);
  }

  .contact-list {
    position: absolute;
    margin: 0;
    padding: 0;
    list-style: none;
    color: var(--white);
    font-size: 32px;
  }
  .contact-list.direct { left: 38px; top: 104px; }
  .contact-list.social { left: 683px; top: 104px; }
  .contact-item {
    display: flex;
    align-items: center;
    height: 46px;
    margin-bottom: 25px;
  }
  .contact-icon {
    flex: none;
    width: 40px;
    height: 40px;
    fill: var(--white);
  }
  .direct .contact-icon { margin-right: 60px; }
  .social .contact-icon { margin-right: 29px; }
  .social-square {
    flex: none;
    width: 38px;
    height: 38px;
    margin-right: 31px;
    background: var(--white);
  }
</style>
</head>
<body>
<main class="card">

  <header class="brand">
    <span class="brand-mark" aria-hidden="true"></span>
    <h1 class="brand-name">
      <span class="line-name">Miranda Voss</span>
      <span class="line-trade">Coaching &amp; Consulting</span>
    </h1>
  </header>

  <section class="person">
    <h2 class="person-name">Miranda Voss</h2>
    <p class="person-role">Principal Coach &amp; Consultant</p>
  </section>

  <div class="divider"></div>

  <section class="contact-band">
    <ul class="contact-list direct">
      <li class="contact-item">
        <svg class="contact-icon" viewBox="0 0 40 40" aria-hidden="true">
          <path d="M9 4 L15 4 L18 12 L14 15 Q17 23 25 27 L28 23 L36 26 L36 32 Q35 37 29 36 Q8 32 4 10 Q4 5 9 4 Z"/>
        </svg>
        <span>0491 362 815</span>
      </li>
      <li class="contact-item">
        <svg class="contact-icon" viewBox="0 0 40 40" aria-hidden="true">
          <path d="M2 9 H38 V11 L20 23 L2 11 Z M2 14 L20 26 L38 14 V32 H2 Z"/>
        </svg>
        <span>miranda.voss@quillmail.example</span>
      </li>
      <li class="contact-item">
        <svg class="contact-icon" viewBox="0 0 40 40" aria-hidden="true">
          <g fill="none" stroke="#ffffff" stroke-width="4.5" stroke-linecap="round">
            <path d="M17 23 L23 17"/>
            <path d="M15 19 L9 25 Q5 29 9 33 Q12 36 16 32 L21 27"/>
            <path d="M25 21 L31 15 Q35 11 31 7 Q28 4 24 8 L19 13"/>
          </g>
        </svg>
        <span>www.mirandavoss.example</span>
      </li>
    </ul>

    <ul class="contact-list social">
      <li class="contact-item">
        <span class="social-square" aria-hidden="true"></span>
        <span>friendbook.example/mirandavoss</span>
      </li>
      <li class="contact-item">
        <span class="social-square" aria-hidden="true"></span>
        <span>chirper.example/mirandavoss</span>
      </li>
      <li class="contact-item">
        <span class="social-square" aria-hidden="true"></span>
        <span>linkpro.example/mirandavoss</span>
      </li>
    </ul>
  </section>

</main>
</body>
</html>
```